Business Card Design for Animal Clinic

We are seeking a two sided business card design. The primary side should include our logo (provided in AI and EPS files) address, phone, website, and if possible "Follow Us" with icons for Facebook, Google+, and Twitter.

The back of the card needs to included space for appointment reminders.

Company Name:
Calderbrook Animal Clinic

Doctor Name:
To be provided to winner

Adress:
To be provided to winner

Phone:
to be provided to winner

Website:
www.calderbrookanimalclinic.com

```html
<!DOCTYPE html>
<html lang="en">
<head>
<meta charset="utf-8">
<title>Calderbrook Animal Clinic – Business Card</title>
<link rel="stylesheet" href="https://fonts.googleapis.com/css2?family=Federo&family=Poiret+One&family=Libre+Baskerville:wght@700&family=Special+Elite&display=swap">
<style>
  :root {
    --backdrop: #a9b8b7;
    --frame: #9e1b1f;
    --frame-dark: #7f1418;
    --paper: #ffffff;
    --band: #c04a30;
    --blush: #f4e0db;
    --tagline: #c0583c;
    --art: #a3191c;
    --art-faint: #f2dad5;
    --ink-white: #ffffff;
    --phone-ink: #7f1418;
  }
  * { box-sizing: border-box; margin: 0; padding: 0; }
  html, body {
    width: 1200px; height: 900px; overflow: hidden;
    background: var(--backdrop);
  }
  .canvas { position: relative; width: 1200px; height: 900px; }

  .card {
    position: absolute; left: 175px; width: 855px;
    background: var(--frame);
    border: 2px solid var(--frame-dark);
    padding: 9px;
  }
  .card--front { top: 0; height: 436px; }
  .card--back { top: 463px; height: 437px; }

  .card__face {
    position: relative; width: 100%; height: 100%;
    background: var(--paper); overflow: hidden;
  }

  .name {
    position: absolute; left: 0; right: 0; text-align: center;
    font-family: "Federo", sans-serif; font-weight: 400;
    color: var(--frame); line-height: 1; white-space: nowrap;
  }
  .tagline {
    position: absolute; font-family: "Poiret One", sans-serif;
    color: var(--tagline); line-height: 1; white-space: nowrap;
    letter-spacing: 3px;
  }

  .art { position: absolute; border-radius: 40% 40% 18% 18%; }
  .art--main { background: var(--art); }
  .art--faint { background: var(--art-faint); }
  .art--corner { background: var(--art); border-radius: 45% 45% 20% 20%; }

  /* Front */
  .card--front .name { top: 30px; font-size: 92px; letter-spacing: 3px; }
  .card--front .tagline { top: 186px; font-size: 42px; }
  .tagline--left { right: 522px; }
  .tagline--right { left: 562px; }
  .card--front .art--main { left: 330px; top: 124px; width: 228px; height: 146px; }

  .contact-band {
    position: absolute; left: 0; right: 0; bottom: 0; height: 116px;
    background: linear-gradient(to bottom, var(--paper) 0, var(--band) 20px, var(--band) 100%);
    color: var(--ink-white); text-align: center;
  }
  .contact-band__address {
    position: absolute; top: 24px; left: 0; right: 0;
    font-family: "Libre Baskerville", serif; font-weight: 700; font-size: 20px;
  }
  .contact-band__phone {
    position: absolute; top: 55px; left: 0; right: 0;
    display: flex; justify-content: center; align-items: center; gap: 40px;
  }
  .plus { font-family: Arial, sans-serif; font-weight: 700; font-size: 28px; line-height: 1; }
  .phone-number {
    font-family: "Special Elite", monospace; font-size: 24px; line-height: 1.1;
    color: var(--phone-ink); background: var(--ink-white);
    padding: 0 6px; letter-spacing: 3px; border-radius: 3px;
  }
  .contact-band__web {
    position: absolute; top: 85px; left: 0; right: 0;
    font-family: Arial, Helvetica, sans-serif; font-weight: 700; font-size: 21px;
  }
  .card--front .art--corner { top: 50px; width: 84px; height: 48px; }
  .card--front .art--corner.left { left: 19px; }
  .card--front .art--corner.right { right: 19px; }

  /* Back */
  .header-band {
    position: absolute; left: 0; right: 0; top: 0; height: 135px;
    background: linear-gradient(to bottom, var(--blush) 0, var(--blush) 110px, var(--paper) 135px);
  }
  .card--back .name { top: 14px; font-size: 70px; letter-spacing: 2px; }
  .card--back .tagline {
    left: 0; right: 0; top: 76px; text-align: center; font-size: 38px;
  }
  .tagline__plus { font-family: Arial, sans-serif; font-weight: 700; color: var(--frame); font-size: 30px; margin: 0 8px; }
  .card--back .art--faint { left: 204px; top: 151px; width: 395px; height: 215px; }
  .card--back .art--corner { top: 351px; width: 90px; height: 50px; }
  .card--back .art--corner.left { left: 19px; }
  .card--back .art--corner.right { right: 19px; }
</style>
</head>
<body>
<main class="canvas">
  <section class="card card--front" aria-label="Card front">
    <div class="card__face">
      <h1 class="name">CALDERBROOK</h1>
      <span class="tagline tagline--left">ANIMAL</span>
      <div class="art art--main" role="img" aria-label="Illustration of a dog, rabbit and cat seen from behind with small hearts"></div>
      <span class="tagline tagline--right">CLINIC</span>
      <div class="contact-band">
        <div class="art art--corner left" role="img" aria-label="Small pet trio illustration"></div>
        <p class="contact-band__address">418 N. Larkspur Road, Fernhollow Springs, FL 32790</p>
        <p class="contact-band__phone">
          <span class="plus">+</span>
          <span class="phone-number">(407) 555-0148</span>
          <span class="plus">+</span>
        </p>
        <p class="contact-band__web">www.calderbrookanimalclinic.com</p>
        <div class="art art--corner right" role="img" aria-label="Small pet trio illustration"></div>
      </div>
    </div>
  </section>

  <section class="card card--back" aria-label="Card back, appointment space">
    <div class="card__face">
      <div class="header-band"></div>
      <h2 class="name">CALDERBROOK</h2>
      <p class="tagline">ANIMAL<span class="tagline__plus">+</span>CLINIC</p>
      <div class="art art--faint" role="img" aria-label="Faint illustration of a dog, rabbit and cat seen from behind"></div>
      <div class="art art--corner left" role="img" aria-label="Small pet trio illustration"></div>
      <div class="art art--corner right" role="img" aria-label="Small pet trio illustration"></div>
    </div>
  </section>
</main>
</body>
</html>
```